The Kestrowe Banner Ad

The Kestrowe (www.thekestrowe.example) is a news-based website in South China that also features dining and nightlife listings, events, jobs, classifieds and more. The cities we cover are Guangzhou and Shenzhen. We have the rare opportunity to have an advertisement placed on the website of the leading English newspaper in Asia. It is a captive audience of people already reading news, so we want to draw their attention to an alternative site for information.

The ad copy is:

Want more China?
The latest news, dining, nightlife, and jobs.
Guangzhou and Shenzhen
The Kestrowe (with a button saying "Check it out")

(Or something like that... you have freedom to adjust the wording).

The dimensions are 300 x 250 px, with a file size <30kb in JPEG/Animated GIF.

```html
<!DOCTYPE html>
<html lang="en">
<head>
<meta charset="utf-8">
<title>The Kestrowe Banner Ad</title>
<link rel="stylesheet" href="https://fonts.googleapis.com/css2?family=PT+Sans:wght@400;700&family=PT+Sans+Narrow:wght@400;700&display=swap">
<style>
  :root {
    --stage: #2a2a2a;
    --paper: #ffffff;
    --ink: #1a1a1a;
    --headline: #ffffff;
    --accent-yellow: #fff200;
    --panel-red: #a30a0a;
    --panel-red-dark: #7a0202;
    --button-top: #ffb03a;
    --button-bottom: #e85f00;
    --button-edge: #c24e00;
  }
  * { box-sizing: border-box; margin: 0; padding: 0; }
  html, body { width: 1200px; height: 554px; overflow: hidden; }
  body {
    background: var(--stage);
    font-family: "PT Sans", Arial, sans-serif;
    position: relative;
  }
  .banner {
    position: absolute;
    top: 99px;
    width: 427px;
    height: 356px;
    background: var(--paper);
    box-shadow: 0 6px 22px rgba(0,0,0,0.6);
    overflow: hidden;
  }
  .banner--city { left: 119px; }
  .banner--panel { left: 649px; }

  .visual {
    position: absolute;
    left: 0; top: 0;
    width: 427px; height: 278px;
  }
  .banner--city .visual {
    background: linear-gradient(180deg, #1a63c4 0%, #4ba6d9 28%, #8aa6b8 50%, #4d5666 72%, #2a2d38 100%);
  }
  .banner--panel .visual {
    background: linear-gradient(180deg, #3b3a7a 0%, #6d5a9c 35%, #4a4e8a 60%, #6f5e9a 80%, #2c2d55 100%);
  }
  .panel-shape { position: absolute; left: 0; top: 0; }

  .city-copy {
    position: absolute;
    left: 0; right: 0; top: 8px;
    text-align: center;
    color: var(--headline);
    text-shadow: 0 2px 3px rgba(0,0,0,0.55);
  }
  .city-copy .headline {
    font-size: 35px; font-weight: 700; letter-spacing: -0.5px; line-height: 1.05;
  }
  .city-copy .lede {
    font-size: 24px; font-weight: 700; line-height: 1.05; margin-top: 2px;
  }
  .city-copy .cities {
    color: var(--accent-yellow);
    font-size: 21px; font-weight: 700; margin-top: 6px;
  }

  .panel-copy {
    position: absolute;
    left: 218px; width: 204px; top: 8px;
    text-align: center;
    font-family: "PT Sans Narrow", "Arial Narrow", sans-serif;
    color: var(--headline);
    text-shadow: 0 2px 3px rgba(0,0,0,0.45);
  }
  .panel-copy .headline { font-weight: 700; line-height: 0.98; }
  .panel-copy .headline span { display: block; }
  .panel-copy .headline .small { font-size: 42px; }
  .panel-copy .headline .large { font-size: 58px; }
  .panel-copy .lede { font-size: 23px; line-height: 1.1; margin-top: 10px; }
  .panel-copy .cities {
    color: var(--accent-yellow);
    font-size: 27px; line-height: 1.02; margin-top: 12px;
  }

  .footer-bar {
    position: absolute;
    left: 0; bottom: 0;
    width: 427px; height: 78px;
    background: var(--paper);
  }
  .brand {
    position: absolute;
    left: 10px; top: 22px;
    display: flex; align-items: center; gap: 6px;
    font-family: "PT Sans", Arial, sans-serif;
    font-size: 26px; font-weight: 700;
    color: var(--ink);
    white-space: nowrap;
  }
  .brand-dot {
    width: 10px; height: 10px; border-radius: 50%;
    background: var(--panel-red);
  }
  .cta {
    position: absolute;
    right: 6px; top: 17px;
    width: 184px; height: 44px;
    border-radius: 7px;
    background: linear-gradient(180deg, var(--button-top) 0%, #f68a10 50%, var(--button-bottom) 100%);
    border: 1px solid var(--button-edge);
    box-shadow: 0 2px 3px rgba(0,0,0,0.25);
    display: flex; align-items: center; justify-content: center; gap: 7px;
    color: #fff;
    font-size: 20px; font-weight: 700;
    text-shadow: 0 1px 1px rgba(0,0,0,0.35);
    white-space: nowrap;
  }
  .cta svg { flex: none; }
</style>
</head>
<body>

  <div class="banner banner--city">
    <div class="visual" role="img" aria-label="Evening skyline of Guangzhou with a lit stadium and city lights"></div>
    <div class="city-copy">
      <p class="headline">WANT MORE CHINA?</p>
      <p class="lede">The latest news, dining,<br>nightlife and jobs.</p>
      <p class="cities">GUANGZHOU AND SHENZHEN</p>
    </div>
    <div class="footer-bar">
      <div class="brand"><span class="brand-dot"></span>The Kestrowe</div>
      <div class="cta">CHECK IT OUT
        <svg width="20" height="20" viewBox="0 0 20 20" aria-hidden="true">
          <circle cx="10" cy="10" r="9" fill="#fff"/>
          <path d="M8 5.5 L12.5 10 L8 14.5" fill="none" stroke="#e06a00" stroke-width="2.6" stroke-linecap="round" stroke-linejoin="round"/>
        </svg>
      </div>
    </div>
  </div>

  <div class="banner banner--panel">
    <div class="visual" role="img" aria-label="Shenzhen towers lit at dusk reflected on the river"></div>
    <svg class="panel-shape" width="427" height="278" viewBox="0 0 427 278" aria-hidden="true">
      <defs>
        <linearGradient id="panelFill" x1="0" y1="0" x2="1" y2="1">
          <stop offset="0" stop-color="var(--panel-red)"/>
          <stop offset="1" stop-color="var(--panel-red-dark)"/>
        </linearGradient>
      </defs>
      <path d="M180,0 Q234,120 206,278 L427,278 L427,0 Z" fill="#a30a0a"/>
      <path d="M180,0 Q234,120 206,278" fill="none" stroke="#ffffff" stroke-width="6"/>
    </svg>
    <div class="panel-copy">
      <p class="headline"><span class="small">WANT MORE</span><span class="large">CHINA?</span></p>
      <p class="lede">The latest news,<br>dining, nightlife<br>and jobs.</p>
      <p class="cities">GUANGZHOU<br>AND SHENZHEN</p>
    </div>
    <div class="footer-bar">
      <div class="brand"><span class="brand-dot"></span>The Kestrowe</div>
      <div class="cta">CHECK IT OUT
        <svg width="20" height="20" viewBox="0 0 20 20" aria-hidden="true">
          <circle cx="10" cy="10" r="9" fill="#fff"/>
          <path d="M8 5.5 L12.5 10 L8 14.5" fill="none" stroke="#e06a00" stroke-width="2.6" stroke-linecap="round" stroke-linejoin="round"/>
        </svg>
      </div>
    </div>
  </div>

</body>
</html>
```